Professional Business Cards for Recruiting Company

We'd like professional 2-sided business cards that reflect a color scheme that matches our website, www.queryvantline.com, and / or logo that is attached.

Slogan used is "We Know People", but needs to be editable because we change it up to "We Know Developers", "We Speak Geek", etc.

Must includes logo, slogan, first and last name, address, email, mobile number and website address.

Files attached for ideas.

Thanks!

Contact Information for Business Card

Logo, Company name, First name, Last name, addresss, email, phone, website address.

Font styles to use
Sans Serif

Colors
0054AA
0677BA
7BADD7
CADEEF
E8F1F8

Requirements
Nice to have
• I do like the following designs. 22962062 and 22962651. Couple ideas anyway.

```html
<!DOCTYPE html>
<html lang="en">
<head>
<meta charset="utf-8">
<title>Queryvant Business Card</title>
<link href="https://fonts.googleapis.com/css2?family=Montserrat:wght@400;500;600&display=swap" rel="stylesheet">
<style>
  :root {
    --card-blue: #104883;
    --ink-white: #ffffff;
    --backdrop: #e9e9e9;
    --shadow: rgba(0, 0, 0, 0.28);
  }
  * { box-sizing: border-box; margin: 0; padding: 0; }
  html, body {
    width: 1200px; height: 1063px; overflow: hidden;
    background: var(--backdrop);
    font-family: "Montserrat", Arial, sans-serif;
    color: var(--ink-white);
  }
  .canvas { position: relative; width: 1200px; height: 1063px; }
  .card {
    position: absolute; left: 300px; width: 600px; height: 344px;
    background: var(--card-blue);
    box-shadow: 0 14px 30px var(--shadow);
  }
  .card-front { top: 188px; }
  .card-back { top: 581px; }

  /* front: brand */
  .brand { position: absolute; left: 42px; top: 52px; display: flex; align-items: center; gap: 12px; }
  .brand-square { width: 22px; height: 22px; background: var(--ink-white); }
  .brand-name { font-size: 26px; font-weight: 400; letter-spacing: 0.5px; line-height: 1; }
  .brand-tagline {
    position: absolute; left: 76px; top: 89px;
    font-size: 6.5px; font-weight: 600; letter-spacing: 1.1px;
  }

  /* front: person */
  .person { position: absolute; right: 42px; top: 176px; text-align: right; }
  .person-name { font-size: 23px; font-weight: 400; letter-spacing: 1px; line-height: 1; }
  .person-name strong { font-weight: 600; }
  .person-title { font-size: 14px; font-weight: 400; margin-top: 9px; letter-spacing: 0.3px; }

  .divider { position: absolute; left: 42px; right: 42px; top: 226px; height: 1px; background: var(--ink-white); }
  .divider-accent { position: absolute; right: 42px; top: 225px; width: 152px; height: 4px; background: var(--ink-white); }

  /* front: contacts */
  .address { position: absolute; left: 42px; top: 238px; display: flex; gap: 6px; }
  .address-text { font-size: 13px; line-height: 19px; letter-spacing: 0.2px; }
  .contact-list { position: absolute; right: 42px; top: 238px; list-style: none; }
  .contact-item {
    display: flex; justify-content: flex-end; align-items: center; gap: 5px;
    font-size: 13px; height: 24px; letter-spacing: 0.2px;
  }
  .icon { width: 17px; height: 17px; flex: none; }

  /* back */
  .back-brand {
    position: absolute; left: 0; right: 0; top: 120px;
    display: flex; justify-content: center; align-items: center; gap: 16px;
  }
  .back-brand-square { width: 36px; height: 36px; background: var(--ink-white); }
  .back-brand-name { font-size: 44px; font-weight: 600; letter-spacing: 1px; line-height: 1; }
  .back-divider { position: absolute; left: 56px; right: 58px; top: 271px; height: 1px; background: var(--ink-white); }
  .back-divider-accent { position: absolute; left: 224px; width: 151px; top: 270px; height: 4px; background: var(--ink-white); }
  .slogan {
    position: absolute; left: 0; right: 0; top: 288px; text-align: center;
    font-size: 17px; font-weight: 400; letter-spacing: 0.8px;
  }
</style>
</head>
<body>
<main class="canvas">
  <section class="card card-front" aria-label="Business card front">
    <div class="brand">
      <span class="brand-square"></span>
      <span class="brand-name">QUERYVANT</span>
    </div>
    <p class="brand-tagline">PROFESSIONAL SOURCING AND RECRUITING</p>

    <div class="person">
      <p class="person-name"><strong>DANA</strong> WHITLOCK</p>
      <p class="person-title">CEO/Owner</p>
    </div>

    <div class="divider"></div>
    <div class="divider-accent"></div>

    <div class="address">
      <svg class="icon" viewBox="0 0 17 17" aria-hidden="true">
        <rect width="17" height="17" rx="2.5" fill="#fff"/>
        <path d="M3 9 L8.5 4 L14 9 M5 8 V13.5 H7.5 V10.5 H9.5 V13.5 H12 V8" fill="none" stroke="#104883" stroke-width="1.6"/>
      </svg>
      <p class="address-text">123, Your Street Name, your<br>city, lane 00125</p>
    </div>

    <ul class="contact-list">
      <li class="contact-item">123-456-7899
        <svg class="icon" viewBox="0 0 17 17" aria-hidden="true">
          <rect width="17" height="17" rx="2.5" fill="#fff"/>
          <path d="M5 3.5 L7 6.5 L6 8 C7 10 8 11 9.5 12 L11 11 L14 13 L12.5 14.5 C8.5 14 3.5 9 3 5 Z" fill="#104883"/>
        </svg>
      </li>
      <li class="contact-item">info@queryvantline.com
        <svg class="icon" viewBox="0 0 17 17" aria-hidden="true">
          <rect width="17" height="17" rx="2.5" fill="#fff"/>
          <rect x="3" y="5" width="11" height="8" fill="none" stroke="#104883" stroke-width="1.3"/>
          <path d="M3 5 L8.5 9.5 L14 5" fill="none" stroke="#104883" stroke-width="1.3"/>
        </svg>
      </li>
      <li class="contact-item">www.queryvantline.com
        <svg class="icon" viewBox="0 0 17 17" aria-hidden="true">
          <rect width="17" height="17" rx="2.5" fill="#fff"/>
          <path d="M5 3 L5 13 L7.5 10.5 L9.5 14.5 L11 13.8 L9 10 L12.5 10 Z" fill="#104883"/>
        </svg>
      </li>
    </ul>
  </section>

  <section class="card card-back" aria-label="Business card back">
    <div class="back-brand">
      <span class="back-brand-square"></span>
      <span class="back-brand-name">QUERYVANT</span>
    </div>
    <div class="back-divider"></div>
    <div class="back-divider-accent"></div>
    <p class="slogan">WE KNOW PEOPLE</p>
  </section>
</main>
</body>
</html>
```